Partnering collective needs a range of stationary to match with a logo

My business group is a collective of Partnership brokers. We would with organisations that are trying to collaborate or partner more effectively, and we support conversations about power, control, equity, transparency, and fit-for-purposes processes for better collaboration. We had a logo developed by a designer on this site a few years ago. We now need the following, to go with the logo:
1. A Powerpoint presentation template. This template should utilise the logo and colours, and should give a range of options for slide layout in a Master slide set, including slides with images/pictures. It would be good if the colour palette varied throughout the slide, or through the slide options. We often work in situations where people are having challenging and difficult conversations, so the presentation of the Powerpoint needs to be calming and reflective, even though the colours we are using are quite vibrant.
2. A report template using the logo, which allows us to have a cover page, and the logo in either a head/footer or as a watermark on a page throughout the rest of the document. We often write bids or proposals, which we would use this layout for. We also write reports and partnering agreement documents, which we would use this document for.
3. A letterhead using our logo, for professional looking letters. We don't have one business address, there are a few of us using the logo in different locations, so we would need a letter template that allows us to input our own address/details.
Thank you!

Target Market(s)

We work with NGos, government departments, scientists, private sector, health and education institutions, academics.

Font styles to use
Other font styles liked:
• Calibri

Requirements
Nice to have
• So far the designs I have received have been too corporate looking. What we do is almost like counselling, except between organisations, not individuals. The powerpoint template needs to look gentle, calming, soothin, rather than dynamic and aggressive. Would be good to use more of the light blues and maroon in the logo, not such overpowering orange. f
Should not have
• The powerpoint template doesn't need to have corporate slides. graphs, profit projections, market analysis, that kind of thing. We don't do corporate work. We do people to people work. Most or our slides will just have text and photos.

```html
<!DOCTYPE html>
<html lang="en">
<head>
<meta charset="utf-8">
<title>Letterhead – the Bridgeway Circle</title>
<link rel="stylesheet" href="https://fonts.googleapis.com/css2?family=Montserrat:wght@400;500;700&family=Raleway:wght@400&family=Open+Sans:wght@700&display=swap">
<style>
  :root {
    --orange: #f7901e;
    --ink: #5d5d60;
    --ink-soft: #77787b;
    --paper: #ffffff;
    --sig-tone: #e9e9ec;
  }
  * { margin: 0; padding: 0; box-sizing: border-box; }
  html, body { width: 907px; height: 1200px; overflow: hidden; background: var(--paper); }
  .letterhead {
    position: relative;
    width: 907px;
    height: 1200px;
    background: var(--paper);
    font-family: "Raleway", sans-serif;
    color: var(--ink);
  }
  .brand-name {
    position: absolute;
    left: 44px;
    top: 80px;
    font-family: "Montserrat", sans-serif;
    font-weight: 500;
    font-size: 21px;
    line-height: 26px;
    color: var(--orange);
    white-space: nowrap;
  }
  .company-contact {
    position: absolute;
    right: 63px;
    top: 69px;
    list-style: none;
    font-family: "Montserrat", sans-serif;
    font-size: 12.5px;
    line-height: 19px;
    color: var(--ink-soft);
    text-align: right;
  }
  .company-contact li { display: flex; justify-content: flex-end; align-items: center; gap: 4px; }
  .company-contact svg { width: 11px; height: 11px; flex: none; }
  .sender {
    position: absolute;
    left: 54px;
    top: 302px;
    font-family: "Montserrat", sans-serif;
    color: var(--ink-soft);
  }
  .sender-name {
    font-weight: 700;
    font-size: 27px;
    letter-spacing: 0.5px;
    color: var(--orange);
    line-height: 34px;
    margin-bottom: 6px;
  }
  .sender p { font-size: 14.5px; line-height: 27px; }
  .sender .sender-address { line-height: 20px; margin-top: 3px; }
  .letter-date {
    position: absolute;
    right: 47px;
    top: 410px;
    font-family: "Open Sans", sans-serif;
    font-weight: 700;
    font-size: 16.5px;
    color: var(--ink-soft);
  }
  .letter-body {
    position: absolute;
    left: 50px;
    top: 467px;
    width: 810px;
    font-size: 15px;
    letter-spacing: 0.55px;
    line-height: 19.3px;
    text-align: justify;
    color: var(--ink-soft);
  }
  .letter-body p + p { margin-top: 19px; }
  .letter-body p.continued { margin-top: 0; }
  .letter-body p.spaced { margin-top: 38px; }
  .signatory-title {
    position: absolute;
    right: 47px;
    top: 854px;
    font-size: 20px;
    color: var(--ink-soft);
  }
  .signature {
    position: absolute;
    left: 681px;
    top: 902px;
    width: 164px;
    height: 98px;
    background: linear-gradient(135deg, var(--sig-tone), #f6f6f8);
  }
  .page-footer {
    position: absolute;
    left: 0;
    top: 1134px;
    width: 907px;
    height: 24px;
  }
  .page-footer svg { position: absolute; left: 0; top: 0; }
  .footer-address {
    position: absolute;
    left: 0;
    width: 907px;
    top: 0;
    text-align: center;
    font-family: "Montserrat", sans-serif;
    font-size: 17px;
    line-height: 24px;
    color: var(--ink-soft);
  }
</style>
</head>
<body>
<main class="letterhead">
  <header>
    <p class="brand-name">the Bridgeway Circle</p>
    <ul class="company-contact">
      <li>555-303-412
        <svg viewBox="0 0 12 12"><circle cx="6" cy="6" r="6" fill="#f7901e"/><path d="M4 3.2c.4-.3.8-.2 1 .2l.4.8c.1.3 0 .5-.2.7l-.3.2c.3.7.8 1.2 1.5 1.5l.2-.3c.2-.2.4-.3.7-.2l.8.4c.4.2.5.6.2 1-.5.6-1.2.7-2 .3A5 5 0 0 1 3.7 5c-.4-.8-.3-1.4.3-1.8z" fill="#fff"/></svg>
      </li>
      <li>info@bridgewaycircle.com
        <svg viewBox="0 0 12 12"><circle cx="6" cy="6" r="6" fill="#f7901e"/><rect x="3" y="4" width="6" height="4.2" rx=".5" fill="#fff"/><path d="M3.2 4.3 6 6.4l2.8-2.1" fill="none" stroke="#f7901e" stroke-width=".7"/></svg>
      </li>
      <li>www.bridgewaycircle.com
        <svg viewBox="0 0 12 12"><circle cx="6" cy="6" r="6" fill="#f7901e"/><g fill="none" stroke="#fff" stroke-width=".7"><circle cx="6" cy="6" r="3.3"/><ellipse cx="6" cy="6" rx="1.4" ry="3.3"/><path d="M2.7 6h6.6"/></g></svg>
      </li>
    </ul>
  </header>

  <section class="sender">
    <h1 class="sender-name">MARA ELLISON</h1>
    <p>0198-555-274</p>
    <p>info@bridgewaycircle.com</p>
    <p class="sender-address">48 Harbour Row, Suite<br>7 Portland, OR 00000</p>
  </section>

  <time class="letter-date" datetime="2023-12-12">12 December, 2023</time>

  <article class="letter-body">
    <p>Lorem ipsum dolor sit amet, consectetuer adipiscing elit, sed diam nonummy nibh euismod tincidunt ut laoreet dolore magna aliquam erat volutpat. Ut wisi enim ad minim veniam, quis nostrud exerci tation ullamcorper suscipit lobortis nisl ut aliquip ex ea commodo consequat. Duis autem vel eum iriure dolor in hendrerit in vulputate velit esse molestie consequat, vel illum dolore eu feugiat nulla facilisis at vero eros et accumsan et iusto odio dignissim qui blandit praesent luptatum zzril delenit augue duis dolore te feugait nulla facilisi.</p>
    <p>Lorem ipsum dolor sit amet, cons ectetuer adipiscing elit, sed diam nonummy nibh euismod tincidunt ut laoreet dolore magna aliquam erat volutpat. Ut wisi enim ad minim veniam, quis nostrud exerci tation ullamcorper suscipit lobortis nisl ut aliquip ex ea commodo consequat.</p>
    <p class="continued">Lorem ipsum dolor sit amet, consectetuer adipiscing elit, sed diam nonummy nibh euismod tincidunt ut laoreet dolore magna aliquam erat</p>
    <p class="spaced">Lorem ipsum dolor sit amet, cons ectetuer adipiscing elit, sed diam nonummy nibh euismod tincidunt ut laoreet dolore magna aliquam erat volutpat. Ut wisi enim ad minim veniam, quis nostrud exerci tation ullamcorper suscipit lobortis nisl ut aliquip ex ea commodo consequat. Lorem ipsum dolor sit zamet, consectetuer adipiscing elit, sed diam nonummy nibh euismod tincidunt.</p>
  </article>

  <p class="signatory-title">Managing Director</p>
  <div class="signature" role="img" aria-label="Handwritten signature of the managing director"></div>

  <footer class="page-footer">
    <svg width="907" height="24" viewBox="0 0 907 24">
      <polygon points="0,11.5 274,9.5 274,15 0,12.5" fill="#f7901e"/>
      <polygon points="633,9.5 907,11.5 907,12.5 633,15" fill="#f7901e"/>
    </svg>
    <p class="footer-address">Your address, your city, box 88900</p>
  </footer>
</main>
</body>
</html>
```